Stationary and Business Card for Law Firm
Modern, Professional & Sophisticated Law Firm Card
Stationary and Business Card for Law Firm - Law
Creative Brief
Professional
Owen Barker
Partner
482 North Mill Avenue Pelham, Illinois 62904
obarker@barkerwynn.example
www.barkerwynn.example
These cards will be used by three attorneys, so I would like to be able to change the names out. Alternatively, if you could insert the names when providing source files, it would be appreciated. Names are: Owen B. Barker Rosalind P. Barker Natalie K. Wynn Emails are: obarker@barkerwynn.example rbarker@barkerwynn.example nwynn@barkerwynn.example
pbruner27 pbruner27
While I like the look many of the envelopes, the return address must be in the upper right hand corner to meet US Postal regulations. Firm Name/Logo Address City, State Zip (additional design info if you like) I have had similar envelopes on a different project with the Logo address on the lower part of the envelope---the post office refused to accept them.

```html
<!DOCTYPE html>
<html lang="en">
<head>
<meta charset="utf-8">
<title>Barker &amp; Wynn — Business Card</title>
<link href="https://fonts.googleapis.com/css2?family=Cinzel:wght@400;500&family=Montserrat:wght@400;500&display=swap" rel="stylesheet">
<style>
  :root {
    --bg: #e9e9e9;
    --card-white: #ffffff;
    --card-dark: #272727;
    --ink: #222222;
    --ink-soft: #444444;
    --gold: #a88a5a;
    --rule: #333333;
    --light: #f2f2f2;
  }
  * { margin: 0; padding: 0; box-sizing: border-box; }
  html, body { width: 1200px; height: 931px; overflow: hidden; background: var(--bg); }
  body { position: relative; font-family: "Montserrat", sans-serif; color: var(--ink); }

  .card { position: absolute; box-shadow: 0 3px 8px rgba(0,0,0,0.18); overflow: hidden; }

  .card-front { left: 320px; top: 108px; width: 593px; height: 352px; background: var(--card-white); }
  .card-back { left: 315px; top: 513px; width: 566px; height: 350px; background: var(--card-dark); }

  .firm-name { font-family: "Cinzel", serif; font-weight: 400; letter-spacing: 0.5px; line-height: 1; }
  .firm-tagline { font-family: "Cinzel", serif; letter-spacing: 0.6px; line-height: 1; }

  .card-front .firm-name { position: absolute; left: 22px; top: 40px; font-size: 28px; color: var(--ink); }
  .card-front .firm-tagline { position: absolute; left: 110px; top: 72px; font-size: 11px; color: var(--ink); }

  .holder { position: absolute; right: 53px; top: 164px; text-align: right; }
  .holder-name { font-family: "Cinzel", serif; font-size: 28px; color: var(--gold); line-height: 1; letter-spacing: 0.5px; }
  .holder-title { font-size: 14px; color: var(--ink-soft); margin-top: 8px; }

  .divider { position: absolute; left: 22px; right: 53px; top: 200px; height: 2px; background: var(--rule); }

  .contact-list { position: absolute; left: 22px; top: 224px; list-style: none; font-size: 15px; color: var(--ink); }
  .contact-list li { display: flex; align-items: center; height: 21px; }
  .contact-list svg { width: 9px; height: 9px; margin-right: 8px; fill: var(--ink-soft); }

  .address { position: absolute; right: 53px; top: 265px; text-align: right; font-size: 15px; line-height: 21px; color: var(--ink); }

  .front-band { position: absolute; left: 0; bottom: 0; width: 593px; height: 44px; }

  .card-back .brand { position: absolute; left: 0; right: 0; top: 138px; text-align: center; color: var(--light); }
  .card-back .firm-name { font-size: 42px; }
  .card-back .firm-tagline { font-size: 15px; margin-top: 6px; }
</style>
</head>
<body>

<section class="card card-front">
  <div class="firm-name">BARKER &amp; WYNN</div>
  <div class="firm-tagline">ATTORNEYS AT LAW</div>

  <div class="holder">
    <div class="holder-name">OWEN BARKER</div>
    <div class="holder-title">Partner</div>
  </div>

  <div class="divider"></div>

  <ul class="contact-list">
    <li><svg viewBox="0 0 10 10"><path d="M2 0.5 L4 2.5 L3 4 Q4.5 6 6 7 L7.5 6 L9.5 8 L8 9.5 Q3 9 0.5 2 Z"/></svg>555.014.2211</li>
    <li><svg viewBox="0 0 10 10"><rect x="1" y="3" width="8" height="5"/><rect x="3" y="0.5" width="4" height="3"/></svg>555.014.5522</li>
    <li><svg viewBox="0 0 10 10"><path d="M0.5 2 H9.5 V8 H0.5 Z M0.5 2 L5 5.5 L9.5 2" fill="none" stroke="#444" stroke-width="1.2"/></svg>obarker@barkerwynn.example</li>
    <li><svg viewBox="0 0 10 10"><circle cx="5" cy="5" r="4.2" fill="none" stroke="#444" stroke-width="1.2"/><path d="M0.8 5 H9.2 M5 0.8 Q2.5 5 5 9.2 M5 0.8 Q7.5 5 5 9.2" fill="none" stroke="#444" stroke-width="0.8"/></svg>www.barkerwynn.example</li>
  </ul>

  <div class="address">482 North Mill Avenue<br>Pelham, Illinois 62904</div>

  <svg class="front-band" viewBox="0 0 593 44" preserveAspectRatio="none" aria-hidden="true">
    <path d="M0 14 H300 Q318 14 330 6 Q340 0 360 0 H593 V44 H0 Z" fill="#272727"/>
    <path d="M0 20 H304 Q322 20 334 12 Q344 6 362 6 H593 V44 H0 Z" fill="#ffffff"/>
    <path d="M0 16 H302 Q320 16 332 8 Q342 2 361 2 H593" fill="none" stroke="#a88a5a" stroke-width="2"/>
    <path d="M0 22 H306 Q324 22 336 14 Q346 8 364 8 H593 V44 H0 Z" fill="#f4f4f4"/>
    <path d="M312 44 Q330 28 345 20 Q360 12 380 12 H593 V44 Z" fill="#272727"/>
  </svg>
</section>

<section class="card card-back">
  <div class="brand">
    <div class="firm-name">BARKER &amp; WYNN</div>
    <div class="firm-tagline">ATTORNEYS AT LAW</div>
  </div>
</section>

</body>
</html>
```